New Business Card Design Project

I'd like a business card design around the same modern style that I used on my website www.brightnookcs.com
It's gonna be one of those round corners double-sided business cards with maybe a big logo on the front and all the info on the back of the card.

Contact Information for Business Card

Marco Dunhall
425-317-6084
www.brightnookcs.com

www.facebook.com/BrightnookCleaningServices
www.intsgram.com/BrightnookCleaningServices

Requirements
Must have
• it needs to look elegant and modern

```html
<!DOCTYPE html>
<html lang="en">
<head>
<meta charset="utf-8">
<title>Brightnook Cleaning Services – Business Card</title>
<link rel="stylesheet" href="https://fonts.googleapis.com/css2?family=Montserrat:wght@400;500;700;800&display=swap">
<style>
  :root {
    --bg: #e9ebef;
    --card-white: #ffffff;
    --brand-blue: #1e9be3;
    --ink: #222326;
    --back-light: #3b9fe0;
    --back-mid: #1f6fcf;
    --back-dark: #1b3f98;
    --text-on-blue: #ffffff;
    --sparkle: rgba(140, 190, 240, 0.55);
  }
  * { margin: 0; padding: 0; box-sizing: border-box; }
  html, body {
    width: 1200px; height: 800px; overflow: hidden;
    background: var(--bg);
    font-family: "Montserrat", Arial, sans-serif;
  }
  .canvas {
    width: 1200px; height: 800px;
    display: flex; align-items: center; justify-content: center; gap: 48px;
  }
  .card {
    width: 525px; height: 300px;
    border-radius: 16px;
    position: relative; overflow: hidden;
    box-shadow: 0 12px 30px rgba(20, 30, 60, 0.18);
  }
  /* Front */
  .card-front {
    background: var(--card-white);
    display: flex; flex-direction: column; align-items: center; justify-content: center;
  }
  .brand-name {
    font-weight: 800; font-size: 60px; letter-spacing: -1px;
    color: var(--brand-blue); line-height: 1;
  }
  .brand-tagline {
    margin-top: 10px;
    font-weight: 700; font-size: 15px; letter-spacing: 2px;
    color: var(--ink);
  }
  /* Back */
  .card-back {
    background: linear-gradient(200deg, var(--back-light) 0%, var(--back-mid) 45%, var(--back-dark) 100%);
    color: var(--text-on-blue);
  }
  .sparkle-field {
    position: absolute; top: 0; right: 0; width: 320px; height: 190px;
    background: radial-gradient(ellipse at 60% 40%, var(--sparkle) 0%, rgba(140,190,240,0) 70%);
  }
  .contact-block {
    position: absolute; left: 34px; bottom: 34px;
  }
  .person-name {
    font-weight: 700; font-size: 24px; letter-spacing: 0.5px;
    padding-bottom: 8px;
    border-bottom: 1.5px solid var(--text-on-blue);
    width: 300px;
  }
  .contact-list { list-style: none; margin-top: 10px; }
  .contact-item {
    display: flex; align-items: center; gap: 10px;
    font-weight: 500; font-size: 14px; line-height: 1; margin-top: 7px;
  }
  .contact-icon {
    width: 18px; height: 18px; border-radius: 4px;
    background: var(--text-on-blue);
    display: flex; align-items: center; justify-content: center;
    flex-shrink: 0;
  }
  .contact-icon svg { width: 12px; height: 12px; }
</style>
</head>
<body>
<main class="canvas">
  <section class="card card-front" aria-label="Card front">
    <div class="brand-name">Brightnook</div>
    <div class="brand-tagline">CLEANING SERVICES</div>
  </section>

  <section class="card card-back" aria-label="Card back">
    <div class="sparkle-field" role="img" aria-label="Soft scattered sparkle decoration"></div>
    <div class="contact-block">
      <div class="person-name">Marco Dunhall</div>
      <ul class="contact-list">
        <li class="contact-item">
          <span class="contact-icon">
            <svg viewBox="0 0 24 24"><path fill="#1f6fcf" d="M6.6 10.8a15.1 15.1 0 0 0 6.6 6.6l2.2-2.2a1 1 0 0 1 1-.25 11.4 11.4 0 0 0 3.6.57 1 1 0 0 1 1 1V20a1 1 0 0 1-1 1A17 17 0 0 1 3 4a1 1 0 0 1 1-1h3.5a1 1 0 0 1 1 1c0 1.25.2 2.45.57 3.57a1 1 0 0 1-.25 1z"/></svg>
          </span>
          425-317-6084
        </li>
        <li class="contact-item">
          <span class="contact-icon">
            <svg viewBox="0 0 24 24" fill="none" stroke="#1f6fcf" stroke-width="2"><circle cx="12" cy="12" r="9"/><path d="M3 12h18M12 3c3 3 3 15 0 18M12 3c-3 3-3 15 0 18"/></svg>
          </span>
          www.brightnookcs.com
        </li>
        <li class="contact-item">
          <span class="contact-icon"></span>
          BrightnookCleaningServices
        </li>
        <li class="contact-item">
          <span class="contact-icon"></span>
          BrightnookCleaningServices
        </li>
      </ul>
    </div>
  </section>
</main>
</body>
</html>
```